Webpage layout and company logo combination

We are trying to renovate an existing site to make it sharper and sophisticated in appearance. This is the existing site: http://www.kestrelhomesnj.com/agents.html . The new presentation should be bright, sharp, sophisticated and should incorporate two additional menu tabs. The menu tabs will be revised as follows: Property Listings, Property Management, Advisory & Consulting, Local Info, R/E Tools, Our Team (please disregard Korean language characters, which will be installed after English version is completed, separately).

It Company

```html
<!DOCTYPE html>
<html lang="en">
<head>
<meta charset="utf-8">
<title>Kestrel Homes — Property Listings</title>
<link rel="stylesheet" href="https://fonts.googleapis.com/css2?family=Arimo:wght@400;700&family=Open+Sans:wght@400&display=swap">
<style>
  :root {
    --brand: #1ab3e8;
    --ink: #333333;
    --ink-soft: #555555;
    --muted: #777777;
    --rule: #cfcfcf;
    --header-bg: #f5f5f5;
    --panel-bg: #f2f2f2;
    --card-bg: #ebebeb;
    --footer-bar: #e4e4e4;
    --page-bg: #ffffff;
  }
  * { box-sizing: border-box; margin: 0; padding: 0; }
  html, body { width: 976px; height: 1200px; overflow: hidden; background: var(--page-bg); }
  body { font-family: "Arimo", Arial, sans-serif; color: var(--ink); }
  .page { position: relative; width: 1000px; height: 1230px; transform: scale(0.976); transform-origin: 0 0; }
  .abs { position: absolute; }

  .top-stripe { left: 0; top: 0; width: 1000px; height: 7px; background: var(--brand); }
  .site-header { left: 0; top: 7px; width: 1000px; height: 62px; background: var(--header-bg); border-bottom: 1px solid var(--brand); }
  .brand-name { left: 103px; top: 30px; font-size: 15px; font-variant: small-caps; letter-spacing: .3px; color: var(--ink); }
  .main-nav { right: 63px; top: 24px; display: flex; gap: 17px; list-style: none; }
  .main-nav li { font-size: 13px; font-variant: small-caps; color: var(--ink-soft); text-shadow: 0 1px 0 #fff; }
  .main-nav li.is-active { color: var(--brand); }

  .hero-photo { left: 64px; top: 95px; width: 518px; height: 360px; background: linear-gradient(180deg, #e9eef2 0%, #b49a73 40%, #6b7052 62%, #4f9a2c 78%, #5fae33 100%); }
  .hero-panel { left: 582px; top: 95px; width: 354px; height: 360px; background: var(--panel-bg); font-family: "Open Sans", Arial, sans-serif; }
  .hero-shadow { left: 64px; top: 452px; width: 872px; height: 10px; box-shadow: 0 6px 8px -6px rgba(0,0,0,.35); border-radius: 0 0 50% 50%; }
  .spec-list { position: absolute; left: 28px; top: 52px; width: 297px; list-style: none; }
  .spec-list li { display: flex; justify-content: space-between; height: 30px; padding-top: 5px; border-bottom: 1px solid #dedede; font-size: 10px; color: var(--ink); }
  .btn { background: var(--brand); color: #fff; border-radius: 2px; }
  .more-info { left: 27px; top: 257px; width: 70px; height: 24px; font-size: 11px; line-height: 24px; text-align: center; }
  .price { right: 28px; top: 255px; font-size: 18px; color: #111; }
  .slider-dots { right: 38px; top: 308px; display: flex; gap: 6px; }
  .slider-dots span { width: 9px; height: 9px; border-radius: 50%; background: #b9b9b9; }
  .slider-dots span.is-current { background: var(--brand); }

  .feature { top: 490px; width: 270px; }
  .section-title { font-size: 22px; font-weight: 400; color: var(--ink-soft); padding-bottom: 6px; border-bottom: 1px solid #888; }
  .section-title em { font-style: normal; color: var(--brand); }
  .feature p { margin-top: 20px; font-size: 11px; line-height: 14px; color: var(--ink-soft); }

  .featured-title { left: 64px; top: 656px; width: 872px; }
  .listing-card { top: 714px; width: 200px; height: 261px; background: var(--card-bg); box-shadow: 0 1px 4px rgba(0,0,0,.25); padding: 10px; }
  .listing-photo { width: 182px; height: 117px; }
  .listing-card h3 { margin: 13px 0 7px; font-size: 12px; font-weight: 400; color: var(--brand); }
  .listing-facts { list-style: none; margin: 0 4px; }
  .listing-facts li { display: flex; justify-content: space-between; height: 20px; padding: 3px 2px 0; border-bottom: 1px solid #c4c4c4; font-size: 10px; color: var(--muted); }

  .footer-rule { left: 64px; top: 1020px; width: 872px; height: 1px; background: #999; }
  .footer-col { top: 1058px; width: 121px; }
  .footer-col h4 { font-size: 12px; font-weight: 400; color: var(--ink); padding-bottom: 6px; border-bottom: 1px dotted #777; }
  .footer-col ul { list-style: none; margin-top: 7px; }
  .footer-col li { display: flex; align-items: center; gap: 4px; height: 20px; font-size: 10px; color: var(--ink); }
  .footer-divider { left: 677px; top: 1040px; width: 1px; height: 140px; background: #999; }
  .newsletter-label { left: 717px; top: 1058px; font-size: 12px; color: var(--ink); }
  .newsletter-input { left: 718px; top: 1080px; width: 218px; height: 29px; border: 1px solid #c8c8c8; background: #fff; font-size: 9px; font-style: italic; padding: 8px 9px; color: var(--ink); }
  .subscribe { left: 864px; top: 1119px; width: 71px; height: 24px; font-size: 12px; line-height: 24px; text-align: center; }
  .copyright-bar { left: 0; top: 1197px; width: 1000px; height: 33px; background: var(--footer-bar); font-size: 9px; color: var(--ink-soft); padding: 11px 64px; }
</style>
</head>
<body>
<div class="page">
  <div class="abs top-stripe"></div>
  <header class="abs site-header">
    <div class="abs brand-name">Kestrel Homes</div>
    <ul class="abs main-nav">
      <li class="is-active">Property Listings</li>
      <li>Property Management</li>
      <li>Advisory &amp; Consulting</li>
      <li>Local Info</li>
      <li>R/E Tools</li>
      <li>Our Team</li>
    </ul>
  </header>

  <div class="abs hero-photo" role="img" aria-label="Photo of a large two-storey stucco home with a dark roof and a green lawn"></div>
  <section class="abs hero-panel">
    <ul class="spec-list">
      <li><span>Property Type:</span><span>Modern Home</span></li>
      <li><span>Address:</span><span>Woodland Park, NJ 75412</span></li>
      <li><span>House Size:</span><span>1,715 Sq Ft</span></li>
      <li><span>Year Built:</span><span>2011</span></li>
      <li><span>Baths:</span><span>3 Bath</span></li>
      <li><span>Beds:</span><span>2 Bed</span></li>
    </ul>
    <div class="abs btn more-info">more info</div>
    <div class="abs price">$ 1,200,000</div>
    <div class="abs slider-dots"><span></span><span class="is-current"></span><span></span></div>
  </section>
  <div class="abs hero-shadow"></div>

  <section class="abs feature" style="left:64px">
    <h2 class="section-title">Creative <em>Solutions</em></h2>
    <p>Lorem ipsum dolor sit amet, consectetur adipiscing elit. Ut quis ligula velit. Etiam odio quam, lobortis eget porttitor nec, congue in lacus. In venenatis neque a eros laoreet eu placerat erat suscipit. Fusce cursus, erat ut scelerisque condimentum, quam odio ultrices leo.</p>
  </section>
  <section class="abs feature" style="left:366px">
    <h2 class="section-title">Customer <em>Features</em></h2>
    <p>Lorem ipsum dolor sit amet, consectetur adipiscing elit. Ut quis ligula velit. Etiam odio quam, lobortis eget porttitor nec, congue in lacus. In venenatis neque a eros laoreet eu placerat erat suscipit. Fusce cursus, erat ut scelerisque condimentum, quam odio ultrices leo.</p>
  </section>
  <section class="abs feature" style="left:666px">
    <h2 class="section-title">Helpful <em>Services</em></h2>
    <p>Lorem ipsum dolor sit amet, consectetur adipiscing elit. Ut quis ligula velit. Etiam odio quam, lobortis eget porttitor nec, congue in lacus. In venenatis neque a eros laoreet eu placerat erat suscipit. Fusce cursus, erat ut scelerisque condimentum, quam odio ultrices leo.</p>
  </section>

  <h2 class="abs section-title featured-title">Featured Home <em>For Sale</em></h2>

  <article class="abs listing-card" style="left:72px">
    <div class="listing-photo" role="img" aria-label="Photo of a grey home with dormer windows under a blue sky" style="background:linear-gradient(180deg,#6fa6dc 0%,#a9c6e4 35%,#8d8e90 65%,#4c5057 100%)"></div>
    <h3>4545 Guttenberg, NJ</h3>
    <ul class="listing-facts"><li><span>Beds:</span><span>7 bed</span></li><li><span>Baths:</span><span>5 bath</span></li><li><span>House size:</span><span>2,700 Sq Ft</span></li><li><span>Lot size:</span><span>0.19 Acres</span></li></ul>
  </article>
  <article class="abs listing-card" style="left:291px">
    <div class="listing-photo" role="img" aria-label="Photo of a beige stone-fronted home with a front lawn" style="background:linear-gradient(180deg,#7fb2e0 0%,#c9b9a6 35%,#a08b77 65%,#6aa43c 100%)"></div>
    <h3>Fort Lee, NJ</h3>
    <ul class="listing-facts"><li><span>Beds:</span><span>7 bed</span></li><li><span>Baths:</span><span>5 bath</span></li><li><span>House size:</span><span>2,700 Sq Ft</span></li><li><span>Lot size:</span><span>0.19 Acres</span></li></ul>
  </article>
  <article class="abs listing-card" style="left:509px">
    <div class="listing-photo" role="img" aria-label="Photo of a tan Mediterranean-style home with a garden" style="background:linear-gradient(180deg,#6d9fd6 0%,#b58a5e 40%,#7a6a3c 70%,#4f8a2a 100%)"></div>
    <h3>North Arlington, NJ</h3>
    <ul class="listing-facts"><li><span>Beds:</span><span>7 bed</span></li><li><span>Baths:</span><span>5 bath</span></li><li><span>House size:</span><span>2,700 Sq Ft</span></li><li><span>Lot size:</span><span>0.19 Acres</span></li></ul>
  </article>
  <article class="abs listing-card" style="left:727px">
    <div class="listing-photo" role="img" aria-label="Photo of a white colonial home surrounded by trees" style="background:linear-gradient(180deg,#8cb8e6 0%,#4f7a3a 35%,#d9dde0 55%,#6aa043 100%)"></div>
    <h3>Edgewater, NJ</h3>
    <ul class="listing-facts"><li><span>Beds:</span><span>7 bed</span></li><li><span>Baths:</span><span>5 bath</span></li><li><span>House size:</span><span>2,700 Sq Ft</span></li><li><span>Lot size:</span><span>0.19 Acres</span></li></ul>
  </article>

  <div class="abs footer-rule"></div>
  <svg width="0" height="0" style="position:absolute"><symbol id="tick" viewBox="0 0 10 10"><path d="M1 5.5 L4 8.5 L9 1.5" fill="none" stroke="#1ab3e8" stroke-width="2"/></symbol></svg>
  <nav class="abs footer-col" style="left:72px"><h4>Company</h4><ul>
    <li><svg width="10" height="10"><use href="#tick"/></svg>About Us</li>
    <li><svg width="10" height="10"><use href="#tick"/></svg>Services</li>
    <li><svg width="10" height="10"><use href="#tick"/></svg>Clients</li>
    <li><svg width="10" height="10"><use href="#tick"/></svg>Presentation</li></ul></nav>
  <nav class="abs footer-col" style="left:221px"><h4>For Clients</h4><ul>
    <li><svg width="10" height="10"><use href="#tick"/></svg>Sign Up</li>
    <li><svg width="10" height="10"><use href="#tick"/></svg>Forum</li>
    <li><svg width="10" height="10"><use href="#tick"/></svg>Promotions</li></ul></nav>
  <nav class="abs footer-col" style="left:372px"><h4>FAQs</h4><ul>
    <li><svg width="10" height="10"><use href="#tick"/></svg>Support</li>
    <li><svg width="10" height="10"><use href="#tick"/></svg>FAQs</li>
    <li><svg width="10" height="10"><use href="#tick"/></svg>Website</li></ul></nav>
  <nav class="abs footer-col" style="left:522px"><h4>Properties</h4><ul>
    <li><svg width="10" height="10"><use href="#tick"/></svg>Luxury</li>
    <li><svg width="10" height="10"><use href="#tick"/></svg>Residential</li>
    <li><svg width="10" height="10"><use href="#tick"/></svg>Commercial</li>
    <li><svg width="10" height="10"><use href="#tick"/></svg>Hometown</li></ul></nav>
  <div class="abs footer-divider"></div>
  <div class="abs newsletter-label">Newsletter Sign Up:</div>
  <div class="abs newsletter-input">Enter your email here...</div>
  <div class="abs btn subscribe">Subscribe</div>

  <footer class="abs copyright-bar">Copyright © 2014 Kestrel Homes. All Rights Reserved</footer>
</div>
</body>
</html>
```